Designs for a Barrister's chambers

Design stationery (including business card and letterhead) for a barrister's chambers -- similar to a law firm, using the enclosed logo. The current designs are not fit for purpose.

```html
<!DOCTYPE html>
<html lang="en">
<head>
<meta charset="utf-8">
<title>Ledgerstone Chambers – Business Card</title>
<link rel="stylesheet" href="https://fonts.googleapis.com/css2?family=Lato:wght@400;700&family=Arimo:wght@400;700&display=swap">
<style>
  :root {
    --navy: #0f1c36;
    --cyan: #0b9bbd;
    --white: #ffffff;
    --text-soft: #e6ecf2;
    --rule: #3a4a66;
    --backdrop: #2b2624;
  }
  * { margin: 0; padding: 0; box-sizing: border-box; }
  html, body {
    width: 1200px; height: 842px; overflow: hidden;
    background: var(--backdrop);
  }
  .stage {
    position: relative; width: 1200px; height: 842px;
  }
  .card {
    position: absolute;
    width: 540px; height: 340px;
    top: 251px;
    background: var(--navy);
    overflow: hidden;
    box-shadow: 0 12px 30px rgba(0,0,0,0.45);
  }
  /* Contact side */
  .card--contact { left: 40px; }
  .card__band {
    position: absolute; left: 0; width: 100%; height: 14px;
    background: var(--cyan);
  }
  .card__band--top { top: 0; }
  .card__band--bottom { bottom: 0; }
  .contact {
    position: absolute; inset: 14px 0;
    display: flex; flex-direction: column; align-items: center; justify-content: center;
    text-align: center;
    font-family: "Arimo", Arial, sans-serif;
    color: var(--text-soft);
  }
  .contact__name {
    font-family: "Lato", sans-serif; font-weight: 700;
    font-size: 27px; color: var(--cyan); letter-spacing: 0.2px;
  }
  .contact__role { font-size: 14px; margin-top: 2px; }
  .contact__rule {
    width: 120px; height: 1px; background: var(--rule); margin: 10px 0;
  }
  .contact__lines { font-size: 13px; line-height: 1.45; }
  .contact__label { color: var(--cyan); font-weight: 700; }
  .contact__sep { margin: 0 6px; }
  .contact__accent { color: var(--cyan); }
  .contact__address { font-size: 13px; }

  /* Brand side */
  .card--brand { left: 620px; }
  .card__tab {
    position: absolute; background: var(--cyan);
  }
  .card__tab--right { right: 0; top: 62px; width: 22px; height: 40px; }
  .card__tab--left { left: 0; top: 198px; width: 22px; height: 48px; }
  .brand {
    position: absolute; left: 0; top: 0; width: 100%; height: 100%;
    display: flex; align-items: center; justify-content: center; gap: 18px;
  }
  .brand__square {
    width: 58px; height: 58px; background: var(--cyan);
  }
  .brand__name {
    font-family: "Lato", sans-serif; font-weight: 700;
    font-size: 36px; line-height: 1.05; color: var(--white);
  }
</style>
</head>
<body>
<main class="stage">
  <section class="card card--contact">
    <div class="card__band card__band--top"></div>
    <div class="contact">
      <div class="contact__name">Marcus Hollingdale</div>
      <div class="contact__role">Barrister</div>
      <div class="contact__rule"></div>
      <div class="contact__lines">
        <div><span class="contact__label">P:</span> 0207 555 0141<span class="contact__sep">|</span><span class="contact__label">M:</span> 07700 900 312</div>
        <div><span class="contact__label">F:</span> 0207 555 0142<span class="contact__sep">|</span><span class="contact__label">W:</span> www.<span class="contact__accent">ledgerstonechambers</span>.com</div>
        <div><span class="contact__label">E:</span> marcus.hollingdale@ledgerstonechambers.com</div>
      </div>
      <div class="contact__rule"></div>
      <div class="contact__address">42 Carter Lane, London EC4V 5AB</div>
    </div>
    <div class="card__band card__band--bottom"></div>
  </section>

  <section class="card card--brand">
    <div class="card__tab card__tab--right"></div>
    <div class="card__tab card__tab--left"></div>
    <div class="brand">
      <div class="brand__square"></div>
      <div class="brand__name">Ledgerstone<br>Chambers</div>
    </div>
  </section>
</main>
</body>
</html>
```